Borealis Film and Design
Your Moments on Reels
Borealis Film and Design -
Creative Brief
Professional
Peter Vandrell
2187 Kettering Ln. North Pole, Alaska 99612
Peter@borealisfilmanddesign.example
borealisfilmanddesign.example

```html
<!DOCTYPE html>
<html lang="en">
<head>
<meta charset="utf-8">
<title>Borealis Film and Design – Business Card</title>
<link href="https://fonts.googleapis.com/css2?family=Roboto:wght@400;500;700;900&display=swap" rel="stylesheet">
<style>
  :root {
    --backdrop: #d9d9d9;
    --card-white: #ffffff;
    --ink: #1b1f2e;
    --brand-blue: #1f5fc4;
    --deep-blue: #0d2f86;
    --navy: #0a1f5c;
    --silver: #c9ccd2;
    --muted: #2c2c2c;
  }
  * { margin: 0; padding: 0; box-sizing: border-box; }
  html, body {
    width: 1200px; height: 665px; overflow: hidden;
    background: var(--backdrop);
    font-family: "Roboto", Arial, sans-serif;
  }
  .canvas { position: relative; width: 1200px; height: 665px; }
  .card {
    position: absolute; border-radius: 20px; overflow: hidden;
    box-shadow: 0 3px 8px rgba(0,0,0,.25);
  }
  .card svg.art { position: absolute; inset: 0; }
  .card-front { left: 103px; top: 72px; width: 485px; height: 283px; background: var(--card-white); }
  .card-back { left: 629px; top: 271px; width: 475px; height: 286px; background: var(--deep-blue); }

  .brand {
    position: absolute; left: 0; right: 0; top: 42px;
    display: flex; align-items: center; justify-content: center; gap: 10px;
  }
  .brand-dot { width: 28px; height: 28px; border-radius: 50%; background: var(--navy); }
  .brand-name { font-weight: 900; font-size: 26px; color: var(--navy); letter-spacing: .3px; }

  .contact { position: absolute; left: 0; right: 0; text-align: center; color: var(--muted); font-size: 12.5px; line-height: 1.2; }
  .contact-name { top: 146px; color: var(--brand-blue); font-size: 16px; font-weight: 500; }
  .contact-address { top: 171px; }
  .contact-lines {
    top: 189px; display: flex; justify-content: center; gap: 14px; font-size: 11.5px;
  }
  .contact-lines span { display: inline-flex; align-items: center; gap: 4px; }
  .license { position: absolute; right: 26px; top: 226px; color: var(--brand-blue); font-size: 12.5px; line-height: 1.2; }
  .front-url { position: absolute; left: 28px; top: 254px; color: #fff; font-size: 11px; font-weight: 500; }

  .back-brand {
    position: absolute; left: 0; right: 0; top: 30px;
    display: flex; flex-direction: column; align-items: center; gap: 12px;
  }
  .back-dot { width: 116px; height: 116px; border-radius: 50%; background: #15171d; box-shadow: 0 0 0 5px #2b2f38; }
  .back-name { font-weight: 900; font-size: 18px; color: #fff; letter-spacing: .3px; }
  .back-url { position: absolute; left: 28px; top: 240px; color: var(--ink); font-size: 11px; font-weight: 500; }
</style>
</head>
<body>
<main class="canvas">

  <section class="card card-front" aria-label="Business card front">
    <svg class="art" width="485" height="283" viewBox="0 0 485 283" aria-hidden="true">
      <defs>
        <linearGradient id="frontWave" x1="0" y1="0" x2="1" y2="1">
          <stop offset="0" stop-color="#2a6fd6"/>
          <stop offset="1" stop-color="#0d2f86"/>
        </linearGradient>
      </defs>
      <path d="M0 214 C 140 196, 300 246, 485 252 L485 262 C 300 258, 140 210, 0 226 Z" fill="var(--silver)"/>
      <path d="M0 229 C 140 212, 300 262, 485 265 L485 283 L0 283 Z" fill="url(#frontWave)"/>
    </svg>

    <div class="brand">
      <span class="brand-dot"></span>
      <span class="brand-name">BOREALIS FILM AND DESIGN</span>
    </div>

    <p class="contact contact-name">Peter Vandrell</p>
    <p class="contact contact-address">2187 Kettering Ln. North Pole, Alaska 99612</p>
    <p class="contact contact-lines">
      <span>
        <svg width="11" height="11" viewBox="0 0 13 13" aria-hidden="true"><rect x="2" y="1" width="9" height="11" rx="2" fill="var(--brand-blue)"/><rect x="4" y="3" width="5" height="6" fill="#fff"/></svg>
        1-907-555-0184
      </span>
      <span>
        <svg width="11" height="11" viewBox="0 0 13 13" aria-hidden="true"><circle cx="6.5" cy="6.5" r="6" fill="var(--brand-blue)"/><rect x="3" y="4.5" width="7" height="4.5" fill="#fff"/></svg>
        Peter@borealisfilmanddesign.example
      </span>
    </p>

    <p class="license">License No.: 480372</p>
    <p class="front-url">www.borealisfilmanddesign.example</p>
  </section>

  <section class="card card-back" aria-label="Business card back">
    <svg class="art" width="475" height="286" viewBox="0 0 475 286" aria-hidden="true">
      <defs>
        <radialGradient id="backGlow" cx="0.5" cy="0.3" r="0.8">
          <stop offset="0" stop-color="#2f6fe0"/>
          <stop offset="1" stop-color="#0b2a7e"/>
        </radialGradient>
        <linearGradient id="backBand" x1="0" y1="0" x2="0" y2="1">
          <stop offset="0" stop-color="#4a4f59"/>
          <stop offset="1" stop-color="#1e2128"/>
        </linearGradient>
      </defs>
      <rect width="475" height="286" fill="url(#backGlow)"/>
      <path d="M0 228 C 160 226, 340 226, 475 208 L475 286 L0 286 Z" fill="#f2f3f5"/>
      <path d="M0 266 C 160 260, 340 270, 475 248 L475 286 L0 286 Z" fill="url(#backBand)"/>
    </svg>

    <div class="back-brand">
      <span class="back-dot"></span>
      <span class="back-name">BOREALIS FILM AND DESIGN</span>
    </div>
    <p class="back-url">www.borealisfilmanddesign.example</p>
  </section>

</main>
</body>
</html>
```